Harbor Notes

I have written a book which I eventually would like to serve a couple of purposes. The initial purpose was to memorialize life events and lessons from my life to pass on to my grandchildren, in hopes they may learn from the experiences. As I completed the book, I now believe I could remove some of the family specific information as much of the information could be useful to many people.

While I want to book to have a great look for the grandkids, more importantly will be the version that we put on the bookshelf to sell. The cover is obviously the first thing a buyer will see and may or may not peak there interest. I would like to include the attached photo as the cover photo and the title language is also attached. Other than that I am not sure what is the best way to design the cover.

```html
<!DOCTYPE html>
<html lang="en">
<head>
<meta charset="utf-8">
<title>Harbor Notes – Life</title>
<link rel="stylesheet" href="https://fonts.googleapis.com/css2?family=Poppins:wght@500;600;700&family=Fredoka:wght@500;600&display=swap">
<style>
  :root {
    --band-black: #000000;
    --band-red: #fe4646;
    --band-grey: #bdbdbd;
    --band-lightgreen: #80df88;
    --band-green: #22e650;
    --band-blue: #219be2;
    --band-cyan: #77dbe0;
    --band-mint: #7ddfbc;
    --band-yellow: #f7f20e;
    --ink: #111111;
    --white: #ffffff;
    --greeting: #a6ecb0;
  }
  html, body { margin: 0; padding: 0; overflow: hidden; }
  body { width: 1200px; height: 775px; }
  .cover {
    position: relative;
    width: 1200px;
    height: 775px;
    overflow: hidden;
    font-family: "Poppins", sans-serif;
  }
  .band { position: absolute; left: 0; width: 1200px; }
  .band--black { top: 0; height: 60px; background: var(--band-black); }
  .band--red { top: 60px; height: 60px; background: var(--band-red); }
  .band--grey { top: 120px; height: 97px; background: var(--band-grey); }
  .band--lightgreen { top: 217px; height: 104px; background: var(--band-lightgreen); }
  .band--green { top: 321px; height: 96px; background: var(--band-green); }
  .band--blue { top: 417px; height: 90px; background: var(--band-blue); }
  .band--cyan { top: 507px; height: 93px; background: var(--band-cyan); }
  .band--mint { top: 600px; height: 81px; background: var(--band-mint); }
  .band--yellow { top: 681px; height: 94px; background: var(--band-yellow); }

  .spine-title {
    position: absolute;
    left: 20px;
    top: 64px;
    height: 711px;
    margin: 0;
    writing-mode: vertical-rl;
    font-family: "Poppins", sans-serif;
    font-weight: 600;
    font-size: 62px;
    line-height: 1;
    color: var(--ink);
    white-space: nowrap;
    letter-spacing: 5px;
  }

  .greeting {
    position: absolute;
    left: 173px;
    top: 10px;
    margin: 0;
    font-family: "Fredoka", sans-serif;
    font-weight: 600;
    font-size: 31px;
    color: var(--greeting);
  }

  .name {
    position: absolute;
    font-family: "Fredoka", sans-serif;
    font-weight: 600;
    font-size: 25px;
    line-height: 1;
    color: var(--white);
  }

  .tagline {
    position: absolute;
    right: 620px;
    margin: 0;
    font-family: "Fredoka", sans-serif;
    font-weight: 500;
    font-size: 18px;
    color: var(--white);
    text-shadow: 0 0 2px rgba(0,0,0,.6);
    text-align: right;
  }
  .tagline--lead { top: 132px; }
  .tagline--follow { top: 166px; }
  .tagline .emphasis { font-size: 25px; font-weight: 600; }

  .life-title {
    position: absolute;
    left: 294px;
    top: 200px;
    margin: 0;
    font-family: "Fredoka", sans-serif;
    font-weight: 600;
    font-size: 118px;
    line-height: 1;
    color: var(--white);
  }

  .family-photo {
    position: absolute;
    left: 143px;
    top: 324px;
    width: 506px;
    height: 357px;
    background: linear-gradient(180deg, #3d3a36 0%, #5b4a3a 35%, #8b8a8f 60%, #4e5a3a 100%);
  }

  .closing-line {
    position: absolute;
    left: 166px;
    top: 704px;
    margin: 0;
    font-family: "Poppins", sans-serif;
    font-weight: 600;
    font-size: 26px;
    color: var(--ink);
  }
  .closing-line .emphasis { font-size: 33px; }
</style>
</head>
<body>
<main class="cover">
  <div class="band band--black"></div>
  <div class="band band--red"></div>
  <div class="band band--grey"></div>
  <div class="band band--lightgreen"></div>
  <div class="band band--green"></div>
  <div class="band band--blue"></div>
  <div class="band band--cyan"></div>
  <div class="band band--mint"></div>
  <div class="band band--yellow"></div>

  <h2 class="spine-title">Harbor Notes - LIFE</h2>

  <p class="greeting">Hi Guys</p>

  <div class="grandchildren">
    <span class="name" style="left:189px; top:64px;">Andrew</span>
    <span class="name" style="left:360px; top:64px;">Paul</span>
    <span class="name" style="left:489px; top:64px;">Simon</span>
    <span class="name" style="left:143px; top:86px;">Luke</span>
    <span class="name" style="left:264px; top:86px;">Grant</span>
    <span class="name" style="left:407px; top:86px;">Samuel</span>
    <span class="name" style="left:548px; top:86px;">Benjamin</span>
  </div>

  <p class="tagline tagline--lead">There's a <span class="emphasis">bump</span> in the road ahead....</p>
  <p class="tagline tagline--follow">It's called...</p>

  <h1 class="life-title">Life</h1>

  <div class="family-photo" role="img" aria-label="Photo of a grandfather sitting on the lawn in front of a porch with his seven grandsons"></div>

  <p class="closing-line">This is about having <span class="emphasis">a great one</span>.</p>
</main>
</body>
</html>
```